Design a box that holds medical gloves for paramedics!

We need a design for a box of gloves (nitrile gloves). We are designing this for a specific customer whose name is Brenvo (their logo is attached as image000.1png). We have also attached the current design for the box which we want to change to be specific for Brenvo. Everywhere you see a turtle, replace it with the Brenvo logo. There should be no turtles on the box. The people who use these gloves are paramedics who work in an ambulance. The box should look TOUGH, American, and instill confidence and safety. An American flag alone or one incorporating the eagle from the company logo covering the top of the box (perhaps in the background on the top) would be a nice touch. Do not change anything on the bottom of the box, which is the side with the size chart on it. You can change background color but all the info on the bottom of the box needs to stay there. What you send back should be the box with all sides designed. We need to start showing our customer options right away for this box so please don't hesitate to start. We look forward to working with you.
Updates

The Client has changed his mind regarding the use of an American Flag. This product will be sold world wide, so NO FLAGS AT ALL. We still want the box to look TOUGH. We would like the top of the box to have the Brenvo Logo very LARGE. We would like the Falcon from the logo to be incorporated somehow into the background of the box. So the whole Falcon or wings of the Flacon faded in background might be nice. The color scheme should still be black, red and white. The design should be bold and tough looking. This initial box will be used for black gloves but in the future the box may have blue gloves so we need some part/aspect of the box to be able to change color to blue or white if we change the color of gloves in the box in the future to have blue or white gloves. Please leave bottom of the box as is shown in original photo uploaded. Thanks and sorry for the change this late in the process.

Target Market(s)

The buyer of this product is a Paramedic who works on an ambulance. Medical market. EMS market.

Industry/Entity Type

Medical

Font styles to use
Sans Serif

Colors
ec1f27
ffffff
1b1b1b

Requirements
Must have
• American Flag
• Patriotic
• Brenvo Logo in several places
• Look tough
• Color scheme should be Black, Red and White.

```html
<!DOCTYPE html>
<html lang="en">
<head>
<meta charset="utf-8">
<title>Brenvo Nitrile Examination Gloves – Box Panels</title>
<link rel="stylesheet" href="https://fonts.googleapis.com/css2?family=Open+Sans:wght@400;600;700;800&display=swap">
<style>
  :root{
    --stage:#e1e2cc;
    --black:#1b1b1b;
    --red:#ec1f27;
    --white:#ffffff;
    --grey:#a3a3a5;
    --ink:#1b1b1b;
    --rule:#555555;
  }
  *{box-sizing:border-box;margin:0;padding:0}
  html,body{width:1200px;height:855px;overflow:hidden}
  body{background:var(--stage);font-family:"Open Sans",Arial,sans-serif;position:relative;color:var(--white)}

  .box{position:absolute;left:70px;width:1020px;height:320px}
  .box--top{top:30px}
  .box--bottom{top:445px}

  .face{position:absolute;left:0;top:0;width:880px;height:250px;overflow:hidden;background:var(--black);box-shadow:0 8px 18px rgba(0,0,0,.22)}
  .side{position:absolute;left:0;top:250px;width:880px;height:70px;overflow:hidden;background:var(--black);border-top:1px solid #333;box-shadow:0 8px 18px rgba(0,0,0,.22)}
  .end{position:absolute;left:880px;top:0;width:140px;height:250px;overflow:hidden;background:var(--grey);border-left:1px solid #8a8a8c;box-shadow:0 8px 18px rgba(0,0,0,.22)}

  .rule{position:absolute;height:2px;background:var(--red)}
  .wordmark{position:absolute;font-weight:800;color:var(--ink);letter-spacing:-1px;line-height:1}
  .glove-icon{position:absolute}
  .size-badge{position:absolute;background:var(--red);color:var(--white);font-weight:800;text-align:center}
  .size-label{position:absolute;background:var(--black);color:var(--white);font-size:9px;line-height:14px;height:14px;text-align:center}
  .features{position:absolute;list-style:none;text-align:right;font-size:11px;font-weight:600;color:var(--ink);line-height:14px}
  .features li::after{content:"";display:inline-block;width:5px;height:5px;background:var(--red);border-radius:50%;margin-left:6px;vertical-align:middle}
  .mini-logo{position:absolute;background:var(--red);border-radius:6px}
  .single-use{position:absolute;font-size:9px;color:var(--ink)}

  /* ---------- top face ---------- */
  .falcon-backdrop{position:absolute;left:0;top:0;width:560px;height:250px;
    background:radial-gradient(ellipse at 45% 55%,#3a3a3a 0%,#262626 45%,var(--black) 80%)}
  .brand-square{position:absolute;left:200px;top:28px;width:140px;height:100px;background:var(--red);border-radius:14px;border:3px solid #3b3b3b}
  .top-title{position:absolute;left:170px;top:160px;font-weight:700;font-size:15px}
  .top-count{position:absolute;left:170px;top:184px;font-weight:600;font-size:12px;color:#d8d8d8}

  .grey-face{position:absolute;right:0;top:0;width:320px;height:250px;background:var(--grey)}
  .wordmark--large{left:24px;top:30px;font-size:64px}
  .product-name{position:absolute;left:26px;top:118px;font-weight:800;font-size:22px;color:var(--ink);letter-spacing:1px}
  .product-name sup{font-size:9px}

  /* ---------- side strips ---------- */
  .falcon-fade{position:absolute;inset:0;background:linear-gradient(90deg,var(--black) 0%,#2e2e2e 60%,var(--black) 100%)}
  .side-title{position:absolute;font-weight:700;font-size:14px;white-space:nowrap}
  .side-sub{position:absolute;font-size:9px;color:#cfcfcf;white-space:nowrap}
  .side-count{position:absolute;right:24px;top:26px;font-weight:600;font-size:12px;color:#d8d8d8}

  /* ---------- bottom face ---------- */
  .info{position:absolute;left:28px;top:20px;width:360px}
  .info h2{font-weight:800;font-size:24px;line-height:1.05}
  .info .info-sub{font-size:10px;margin-bottom:10px}
  .info p{font-size:10.5px;line-height:13px;margin-bottom:5px}
  .info strong{font-weight:700}
  .lot-box{position:absolute;left:420px;top:20px;width:260px;height:32px;font-size:8px;font-weight:700}
  .lot-box span{display:block;line-height:16px}
  .lot-box .field{position:absolute;left:56px;top:0;width:200px;height:32px;background:var(--white)}
  .size-chart{position:absolute;left:420px;top:62px;width:430px;height:66px;background:var(--white);color:var(--ink)}
  .ruler{position:absolute;left:10px;right:10px;bottom:14px;height:14px;border-top:1px solid var(--ink);
    background:repeating-linear-gradient(90deg,var(--ink) 0 1px,transparent 1px 8.6px) top/100% 6px no-repeat,
               repeating-linear-gradient(90deg,var(--ink) 0 1px,transparent 1px 34.2px) top/100% 11px no-repeat}
  .ruler-nums{position:absolute;left:8px;right:8px;bottom:2px;display:flex;justify-content:space-between;font-size:7px}
  .hand-zone{position:absolute;left:22px;top:10px;width:40px;height:28px;background:#e8cfa6;border-radius:6px}
  .size-steps{position:absolute;top:6px;font-size:7px}
  .divider{position:absolute;left:420px;right:30px;top:136px;height:1px;background:var(--rule)}
  .certs{position:absolute;left:420px;top:150px;display:flex;gap:10px}
  .cert{width:24px;height:24px;border:2px solid var(--white);border-radius:50%}
  .cert--square{border-radius:3px}
  .made-for{position:absolute;left:500px;top:146px;font-size:8.5px;line-height:11px}
  .made-for b{font-weight:700}
  .origin{position:absolute;right:30px;top:146px;font-size:7px;color:#bbb}

  .grey-band{position:absolute;left:0;top:0;width:560px;height:70px;background:var(--grey)}
  .distributor{position:absolute;left:24px;top:16px;font-weight:800;font-size:26px;line-height:1.3;color:var(--white);letter-spacing:1px}
  .item-no{position:absolute;left:300px;top:18px;font-size:10px;font-weight:700;color:var(--ink)}
  .grey-band .single-use{left:300px;top:36px}
</style>
</head>
<body>

<!-- Box: top, front side and end -->
<div class="box box--top">
  <section class="face" aria-label="Box top">
    <div class="falcon-backdrop" role="img" aria-label="Large faded falcon with spread wings in the background"></div>
    <div class="brand-square" role="img" aria-label="Brenvo brand square"></div>
    <p class="top-title">Nitrile Powder Free Black Examination Gloves</p>
    <p class="top-count">100 Gloves by Weight</p>

    <div class="grey-face">
      <div class="rule" style="left:20px;right:20px;top:18px"></div>
      <div class="wordmark wordmark--large">Brenvo</div>
      <div class="rule" style="left:20px;right:20px;top:104px"></div>
      <div class="product-name">STRIKE<sup>®</sup></div>
      <svg class="glove-icon" style="left:140px;top:112px" width="40" height="44" viewBox="0 0 44 48" aria-hidden="true">
        <path d="M10 46V26l-6-8c-2-3 2-5 4-3l4 5V6c0-3 4-3 4 0v14V3c0-3 4-3 4 0v17V4c0-3 4-3 4 0v16V8c0-3 4-3 4 0v20c0 6-2 10-4 12v6z" fill="none" stroke="var(--ink)" stroke-width="1.5"/>
      </svg>
      <div class="size-badge" style="left:200px;top:110px;width:44px;height:44px;font-size:32px;line-height:44px">L</div>
      <div class="size-label" style="left:200px;top:154px;width:100px">Large</div>
      <ul class="features" style="right:22px;top:176px">
        <li>Textured</li><li>Non-Sterile</li><li>Ambidextrous</li><li>Latex Free</li>
      </ul>
    </div>
  </section>

  <section class="side" aria-label="Box front side">
    <div class="falcon-fade" role="img" aria-label="Faded falcon wings in the background"></div>
    <p class="side-title" style="left:28px;top:14px">Nitrile Powder Free Black Examination Gloves</p>
    <p class="side-sub" style="left:28px;top:38px">Powder free disposable examination gloves made of soft nitrile material</p>
    <p class="side-count">100 Gloves by Weight</p>
  </section>

  <section class="end" aria-label="Box end">
    <div class="mini-logo" style="left:14px;top:20px;width:40px;height:32px"></div>
    <div class="wordmark" style="left:14px;top:62px;font-size:26px">Brenvo</div>
    <div class="rule" style="left:14px;right:14px;top:98px"></div>
    <svg class="glove-icon" style="left:16px;top:112px" width="30" height="34" viewBox="0 0 44 48" aria-hidden="true">
      <path d="M10 46V26l-6-8c-2-3 2-5 4-3l4 5V6c0-3 4-3 4 0v14V3c0-3 4-3 4 0v17V4c0-3 4-3 4 0v16V8c0-3 4-3 4 0v20c0 6-2 10-4 12v6z" fill="none" stroke="var(--ink)" stroke-width="2"/>
    </svg>
    <div class="size-badge" style="left:82px;top:108px;width:40px;height:40px;font-size:28px;line-height:40px">L</div>
    <div class="size-label" style="left:82px;top:148px;width:44px">Large</div>
    <ul class="features" style="right:14px;top:170px;font-size:10px;line-height:13px">
      <li>Textured</li><li>Non-Sterile</li><li>Ambidextrous</li><li>Latex Free</li>
    </ul>
    <div class="single-use" style="left:14px;top:230px">For Single Use</div>
  </section>
</div>

<!-- Box: bottom, back side and end -->
<div class="box box--bottom">
  <section class="face" aria-label="Box bottom">
    <div class="info">
      <h2>Strike</h2>
      <p class="info-sub">Nitrile Powder Free Black Examination Gloves</p>
      <p><strong>Caution:</strong> Material used in glove manufacturing may cause allergic reactions in some users.</p>
      <p><strong>Caution:</strong> Examination gloves are not intended for direct exposure to harsh chemicals.</p>
      <p><strong>Storage:</strong> Avoid storage in direct sunlight/fluorescent lighting and keep area cool, dry, and well ventilated.</p>
      <p><strong>Not made with natural rubber latex.</strong></p>
    </div>

    <div class="lot-box">
      <span>Lot No:</span><span>Expiry Date:</span>
      <div class="field"></div>
    </div>

    <div class="size-chart">
      <div class="hand-zone" role="img" aria-label="Hand placed on the sizing ruler"></div>
      <span class="size-steps" style="left:170px">X-Small</span>
      <span class="size-steps" style="left:212px">Small</span>
      <span class="size-steps" style="left:245px">Medium</span>
      <span class="size-steps" style="left:290px">Large</span>
      <span class="size-steps" style="left:325px">X-Large</span>
      <span class="size-steps" style="left:366px">XX-Large</span>
      <div class="ruler"></div>
      <div class="ruler-nums"><span>0</span><span>1</span><span>2</span><span>3</span><span>4</span><span>5</span><span>6</span><span>7</span><span>8</span><span>9</span><span>10</span><span>11</span><span>12</span></div>
    </div>

    <div class="divider"></div>
    <div class="certs"><div class="cert cert--square"></div><div class="cert"></div></div>
    <div class="made-for">
      <b>Manufactured For</b><br>
      USA<br>
      Norvale Supply, LLC<br>
      1180 Harbor Lane<br>
      Alder OR 97000<br>
      1-800-555-0142<br>
      Fax: 1-541-555-0187<br>
      www.norvalesupply.example
    </div>
    <div class="origin">Made in Malaysia</div>
  </section>

  <section class="side" aria-label="Box back side">
    <div class="falcon-fade" role="img" aria-label="Faded falcon wings in the background"></div>
    <div class="grey-band">
      <div class="distributor">Norvale Supply</div>
      <div class="item-no">Item No. 73004</div>
      <div class="single-use">For Single Use</div>
    </div>
    <p class="side-title" style="left:576px;top:16px;font-size:12px">Nitrile Powder Free Black Examination Gloves</p>
    <p class="side-sub" style="left:576px;top:38px;font-size:8px">Powder free disposable examination gloves made of soft nitrile material</p>
  </section>

  <section class="end" aria-label="Box end">
    <div class="mini-logo" style="left:14px;top:20px;width:40px;height:32px"></div>
    <div class="wordmark" style="left:14px;top:62px;font-size:26px">Brenvo</div>
    <div class="rule" style="left:14px;right:14px;top:98px"></div>
    <svg class="glove-icon" style="left:16px;top:112px" width="30" height="34" viewBox="0 0 44 48" aria-hidden="true">
      <path d="M10 46V26l-6-8c-2-3 2-5 4-3l4 5V6c0-3 4-3 4 0v14V3c0-3 4-3 4 0v17V4c0-3 4-3 4 0v16V8c0-3 4-3 4 0v20c0 6-2 10-4 12v6z" fill="none" stroke="var(--ink)" stroke-width="2"/>
    </svg>
    <div class="size-badge" style="left:82px;top:108px;width:40px;height:40px;font-size:28px;line-height:40px">L</div>
    <div class="size-label" style="left:82px;top:148px;width:44px">Large</div>
    <ul class="features" style="right:14px;top:170px;font-size:10px;line-height:13px">
      <li>Textured</li><li>Non-Sterile</li><li>Ambidextrous</li><li>Latex Free</li>
    </ul>
    <div class="single-use" style="left:14px;top:230px">For Single Use</div>
  </section>
</div>

</body>
</html>
```